Flyer Design Project

We are a storm restoration company that has recently begun restoration from water/flood damage from Hurricane Sandy. We provide disaster relief to homeowners and or commercial property owners after a flood. To start we offer cleanup and remediation which is taking out and disposing of all wet items in a home or business and the cutting out of walls, flooring and other items affected by a flood. We then provide remediation which includes the drying out of a home or business along with a dehumidifier to take all the moisture out of the air and to put it simply dry out the home. We also uses chemicals to clean and provide mold remediation to prevent to growth of mold. We work directly with a customers insurance company if they have flood insurance and after that we provide the services to rebuild and bring their property back to its condition before the storm.

Im looking for an informational type flier that I could insert into our business folders that we give to customers and also to use as fliers to pass out to potential customers. I want potential customers to look at this and feel comfortable with calling my company and working with us.

Company name Bellridge Building Partners. I attached our company logo.

Target Market(s)

Those affected by flooding from Hurricane Sandy

Industry/Entity Type

Insurance

Requirements
Must have
• Company logo, name and colors on flier
Nice to have
• Color photos that have to do with water restoration or showing flood damamge

```html
<!DOCTYPE html>
<html lang="en">
<head>
<meta charset="utf-8">
<title>Bellridge Building Partners – Hurricane Sandy Relief Flyer</title>
<link rel="stylesheet" href="https://fonts.googleapis.com/css2?family=Archivo+Black&family=Mulish:wght@400;700;800&display=swap">
<style>
  :root {
    --navy: #1b2a4c;
    --yellow: #f2e91c;
    --arrow-blue: #3f72b5;
    --white: #ffffff;
    --photo-sky: #c9ccd0;
    --photo-water: #4a5257;
  }
  html, body {
    margin: 0;
    padding: 0;
    width: 972px;
    height: 1200px;
    overflow: hidden;
    background: var(--white);
  }
  .flyer {
    position: relative;
    width: 972px;
    height: 1200px;
    background: var(--white);
    font-family: "Mulish", "Century Gothic", sans-serif;
    color: var(--navy);
  }
  .brand {
    position: absolute;
    left: 100px;
    top: 48px;
    width: 262px;
    display: flex;
    align-items: center;
    gap: 14px;
  }
  .brand-mark {
    flex: 0 0 auto;
    width: 46px;
    height: 46px;
    border-radius: 50%;
    background: var(--navy);
  }
  .brand-name {
    font-family: "Mulish", sans-serif;
    font-weight: 800;
    font-size: 30px;
    line-height: 1.05;
    color: var(--navy);
  }
  .call-out {
    position: absolute;
    left: 440px;
    top: 74px;
    width: 464px;
    text-align: center;
    font-family: "Mulish", sans-serif;
    font-weight: 800;
    font-size: 42px;
    line-height: 52px;
    color: var(--navy);
    letter-spacing: 0.5px;
  }
  .call-out p { margin: 0; }

  .offer-panel {
    position: absolute;
    left: 10px;
    top: 237px;
    width: 956px;
    height: 959px;
    background: var(--yellow);
  }
  .edge {
    position: absolute;
    overflow: hidden;
    color: var(--arrow-blue);
    font-size: 13px;
    line-height: 13px;
    white-space: nowrap;
  }
  .edge-top { left: 0; right: 0; top: -6px; height: 13px; letter-spacing: 16px; }
  .edge-bottom { left: 0; right: 0; bottom: -6px; height: 13px; letter-spacing: 16px; }
  .edge-left, .edge-right { top: 0; bottom: 0; width: 13px; white-space: normal; line-height: 29px; text-align: center; }
  .edge-left { left: -6px; }
  .edge-right { right: -6px; }

  .headline {
    position: absolute;
    left: 0;
    width: 956px;
    text-align: center;
    margin: 0;
    font-family: "Archivo Black", "Arial Black", sans-serif;
    font-weight: 400;
    color: var(--navy);
    letter-spacing: 2px;
  }
  .headline-top { top: 42px; font-size: 96px; line-height: 110px; }
  .headline-bottom { top: 812px; font-size: 96px; line-height: 110px; }
  .subhead {
    position: absolute;
    top: 150px;
    left: 0;
    width: 956px;
    margin: 0;
    text-align: center;
    font-family: "Archivo Black", sans-serif;
    font-size: 24px;
    line-height: 30px;
    color: var(--navy);
  }
  .flood-photo {
    position: absolute;
    left: 12px;
    top: 240px;
    width: 516px;
    height: 336px;
    border: 2px solid var(--navy);
    background: linear-gradient(180deg, var(--photo-sky) 0%, #b9bdc1 55%, #6b7378 72%, var(--photo-water) 100%);
  }
  .process {
    position: absolute;
    left: 540px;
    top: 236px;
    width: 412px;
    text-align: center;
    color: #000;
    font-size: 19.5px;
    line-height: 23.5px;
  }
  .process h2 {
    margin: 0 0 14px;
    font-weight: 800;
    font-size: 23px;
    line-height: 28px;
  }
  .process p { margin: 0 0 23px; }
  .process strong { font-weight: 800; }
  .closing {
    position: absolute;
    left: 14px;
    top: 636px;
    width: 928px;
    margin: 0;
    text-align: center;
    font-weight: 800;
    font-size: 22px;
    line-height: 30px;
    color: #000;
  }
</style>
</head>
<body>
<main class="flyer">
  <header>
    <div class="brand">
      <span class="brand-mark" aria-hidden="true"></span>
      <span class="brand-name">Bellridge Building Partners</span>
    </div>
    <div class="call-out">
      <p>CALL US TODAY</p>
      <p>800-555-ROOF</p>
    </div>
  </header>

  <section class="offer-panel">
    <div class="edge edge-top" aria-hidden="true">→→→→→→→→→→→→→→→→→→→→→→→→→→→→→→→→→→→→</div>
    <div class="edge edge-bottom" aria-hidden="true">←←←←←←←←←←←←←←←←←←←←←←←←←←←←←←←←←←←←</div>
    <div class="edge edge-left" aria-hidden="true">↑ ↑ ↑ ↑ ↑ ↑ ↑ ↑ ↑ ↑ ↑ ↑ ↑ ↑ ↑ ↑ ↑ ↑ ↑ ↑ ↑ ↑ ↑ ↑ ↑ ↑ ↑ ↑ ↑ ↑ ↑ ↑ ↑</div>
    <div class="edge edge-right" aria-hidden="true">↓ ↓ ↓ ↓ ↓ ↓ ↓ ↓ ↓ ↓ ↓ ↓ ↓ ↓ ↓ ↓ ↓ ↓ ↓ ↓ ↓ ↓ ↓ ↓ ↓ ↓ ↓ ↓ ↓ ↓ ↓ ↓ ↓</div>

    <h1 class="headline headline-top">WE CAN HELP!</h1>
    <p class="subhead">We Provide Diaster Relief for Hurricane Sandy</p>

    <div class="flood-photo" role="img" aria-label="Photo of a white wooden cottage standing in floodwater under a grey stormy sky"></div>

    <div class="process">
      <h2>The Restoration Process:</h2>
      <p>-We offer <strong>cleanup and remediation</strong> which requires taking out and disposing of all wet items in a homes/businesses and the cutting out of walls, flooring and other items affected by a flood.</p>
      <p>-When then began the <strong>process of drying out</strong> of a home or business along with a dehumidifier to take all the moisture out of the air and to put it simply dry out the home.</p>
    </div>

    <p class="closing">We also use chemicals to clean and provide mold remediation to prevent to growth of mold. We work directly with a customers insurance company if they have flood insurance and after that we provide the services to rebuild and bring their property back to its condition before the storm.</p>

    <h2 class="headline headline-bottom">LET US HELP!</h2>
  </section>
</main>
</body>
</html>
```